Adult Literacy Program - flyer to attract volunteers and students

We want a flyer that is engaging, colorful, modern and will appeal to our primary audience of adults aged 40-60. We are trying to attract both prospective volunteers (typically age 50+, mostly women) and students (typically aged 40+).
The flyer should feature diverse people working together in pairs of two, reading or talking, with a workbook or some reading material in front of them.

Our organization trains tutors to work one-on-one with adults who are learning how to read. Most of our adult students are non-native speakers of English. Many are of Haitian or Hispanic origin, so we would like some people who represent that demographic.

The Flyer should represent reading, learning, literacy, knowledge, growth,
and opportunities.
Our students are learning to read so they can advance their job opportunities.

Target Market(s)

Adults aged 40-60, primarily women, retired, volunteers

Industry/Entity Type

Education

Font styles to use
Serif
Sans Serif

Colors

Designer to choose colors to be used in the design.

Requirements
Must have
• - UPDATE: Should be designed as a TRI-FOLD brochure on 8.5 x 11 inch paper that will be folded into thirds.
• - Images of diverse people, women and men, who look Hispanic, Haitian and other nationalities as well as Caucasian.
• - Our logo on the front cover
Nice to have
• The sample flyer is very boring and dry! We are open to different ways of presenting the text.

```html
<!DOCTYPE html>
<html lang="en">
<head>
<meta charset="utf-8">
<title>Adult Literacy Program – Tri-fold Inside Spread</title>
<link rel="stylesheet" href="https://fonts.googleapis.com/css2?family=Open+Sans:wght@400;600;700;800&display=swap">
<style>
  :root {
    --navy: #0f2566;
    --navy-deep: #0a1b4f;
    --accent: #1f7fc7;
    --paper: #ffffff;
    --ink: #101a33;
    --stage: #e9eaee;
    --photo-warm-a: #c9a98a;
    --photo-warm-b: #8a6a52;
    --photo-cool-a: #b7c2cf;
    --photo-cool-b: #6f7f92;
  }
  * { box-sizing: border-box; margin: 0; padding: 0; }
  html, body {
    width: 1200px; height: 800px; overflow: hidden;
    background: var(--stage);
    font-family: "Open Sans", Arial, sans-serif;
    color: var(--ink);
  }
  .spread {
    position: absolute; left: 120px; top: 29px;
    width: 960px; height: 742px;
    background: var(--paper);
    box-shadow: 0 10px 30px rgba(0,0,0,.18);
    overflow: hidden;
  }
  .spread-art { position: absolute; inset: 0; }
  .panel { position: absolute; top: 0; width: 320px; height: 742px; }
  .panel--students { left: 0; }
  .panel--about { left: 320px; }
  .panel--why { left: 640px; }

  .students-copy { position: absolute; left: 34px; top: 40px; width: 270px; }
  .section-title {
    font-weight: 800; font-size: 25px; letter-spacing: .5px;
    color: var(--navy); text-transform: uppercase; line-height: 1.1;
  }
  .section-title::after {
    content: ""; display: block; width: 64px; height: 3px;
    background: currentColor; margin-top: 6px;
  }
  .students-lead { font-weight: 700; font-size: 14px; margin-top: 10px; }
  .tick-list { list-style: none; margin-top: 4px; }
  .tick-list li {
    position: relative; padding-left: 22px;
    font-size: 14.5px; line-height: 1.35; margin-bottom: 1px;
  }
  .tick-list--strong { margin-top: 10px; }
  .tick-list--strong li { font-weight: 700; margin-bottom: 3px; }
  .tick-list li::before {
    content: ""; position: absolute; left: 3px; top: 4px;
    width: 6px; height: 11px;
    border: solid var(--navy); border-width: 0 2.5px 2.5px 0;
    transform: rotate(40deg);
  }
  .tagline { margin-top: 16px; color: var(--navy); line-height: 1.1; }
  .tagline-top { font-size: 20px; font-weight: 400; letter-spacing: .5px; text-transform: uppercase; }
  .tagline-main { font-size: 26px; font-weight: 800; text-transform: uppercase; display: block; }

  .panel-copy { position: absolute; left: 40px; width: 250px; color: #fff; }
  .panel--about .panel-copy { top: 470px; }
  .panel--why .panel-copy { top: 380px; }
  .panel-copy .section-title { color: #fff; }
  .panel-copy p { margin-top: 16px; font-size: 13px; line-height: 1.5; }
</style>
</head>
<body>
<main class="spread">
  <svg class="spread-art" width="960" height="742" viewBox="0 0 960 742">
    <defs>
      <linearGradient id="warmPhoto" x1="0" y1="0" x2="1" y2="1">
        <stop offset="0" stop-color="#c9a98a"/>
        <stop offset="1" stop-color="#8a6a52"/>
      </linearGradient>
      <linearGradient id="coolPhoto" x1="0" y1="0" x2="1" y2="1">
        <stop offset="0" stop-color="#b7c2cf"/>
        <stop offset="1" stop-color="#6f7f92"/>
      </linearGradient>
      <linearGradient id="navyBand" x1="0" y1="0" x2="0" y2="1">
        <stop offset="0" stop-color="#14307a"/>
        <stop offset="1" stop-color="#0a1b4f"/>
      </linearGradient>
    </defs>

    <rect x="0" y="472" width="320" height="262" fill="url(#warmPhoto)" role="img" aria-label="Photo: a volunteer tutor and an adult student reading a workbook together at a library table"/>

    <rect x="320" y="0" width="320" height="500" fill="url(#warmPhoto)" role="img" aria-label="Photo: a smiling woman talking with a tutor over an open book"/>

    <rect x="640" y="0" width="320" height="200" fill="url(#coolPhoto)" role="img" aria-label="Photo: tutors and students studying together in a library"/>
    <rect x="640" y="200" width="320" height="220" fill="url(#warmPhoto)" role="img" aria-label="Photo: a diverse group of adult learners smiling at a study table"/>
    <path d="M640 214 Q800 196 960 186" fill="none" stroke="#fff" stroke-width="5"/>

    <path d="M320 470 Q470 400 640 388 L640 742 L320 742 Z" fill="url(#navyBand)"/>
    <path d="M640 388 Q800 330 960 290 L960 742 L640 742 Z" fill="url(#navyBand)"/>
    <path d="M320 470 Q470 400 640 388 Q800 330 960 290" fill="none" stroke="#1f7fc7" stroke-width="3"/>

    <rect x="0" y="730" width="960" height="12" fill="#1f7fc7"/>
    <line x1="320" y1="0" x2="320" y2="742" stroke="rgba(0,0,0,.08)"/>
    <line x1="640" y1="0" x2="640" y2="742" stroke="rgba(0,0,0,.08)"/>
  </svg>

  <section class="panel panel--students">
    <div class="students-copy">
      <h2 class="section-title">Students</h2>
      <p class="students-lead">Students are adults in need of</p>
      <ul class="tick-list">
        <li>basic literacy skills</li>
        <li>pre-HSE skills</li>
        <li>conversational English</li>
      </ul>
      <ul class="tick-list tick-list--strong">
        <li>Tutoring is free of charge</li>
        <li>Tutoring is one-on-one</li>
        <li>Flexible scheduling during library hours</li>
        <li>Lessons focus on student goals</li>
      </ul>
      <p class="tagline">
        <span class="tagline-top">If you can read,</span>
        <strong class="tagline-main">You can tutor!</strong>
      </p>
    </div>
  </section>

  <section class="panel panel--about">
    <div class="panel-copy">
      <h2 class="section-title">About Us</h2>
      <p>Lorem ipsum dolor sit amet, consectetur adipiscing elit, sed do eiusmod tempor incididunt ut labore et dolore magna aliqua. Ut enim ad minim veniam, quis nostrud exercitation ullamco laboris nisi ut aliquip ex ea commodo consequat. Duis aute irure dolor in reprehenderit in voluptate velit esse cillum dolore eu fugiat nulla pariatur.</p>
    </div>
  </section>

  <section class="panel panel--why">
    <div class="panel-copy">
      <h2 class="section-title">Why Choose Us</h2>
      <p>Lorem ipsum dolor sit amet, consectetur adipiscing elit, sed do eiusmod tempor incididunt ut labore et dolore magna aliqua. Ut enim ad minim veniam, quis nostrud exercitation ullamco laboris nisi ut aliquip ex ea commodo consequat. Duis aute irure dolor in reprehenderit in voluptate velit esse cillum dolore eu fugiat nulla pariatur.</p>
    </div>
  </section>
</main>
</body>
</html>
```